Poster design for a company operating care homes in the UK showcasing our core values

We need a poster to display in our care homes showcasing our new core values:

Purpose
We are driven by a clear understanding of why we do what we do: to enrich lives, honour legacies and make a meaningful difference every day, for our residents, their families, our colleagues and our community.

Excellence
We hold ourselves to the highest standards, delivering exceptional care and creating an environment where both residents and staff can thrive.

Openness
We build trust through honest, respectful communication, welcoming feedback, sharing ideas, and embracing change as a path to continuous growth.

Passion
We are passionate about delivering exceptional care. We take pride in what we do and in making a real difference in people’s lives.

Learning
We are committed to personal and professional growth; empowering each other through ongoing development, reflection, and shared knowledge.

Empathy
We actively listen and seek to understand before being understood, recognising the unique stories, feelings, and needs of others.

I have attached a small graphic that we would like you try to incorporate, in addition to our company logo. Please theme the rest of the poster around our company colours.

```html
<!DOCTYPE html>
<html lang="en">
<head>
<meta charset="utf-8">
<title>Halden Care – Our Values</title>
<link href="https://fonts.googleapis.com/css2?family=Montserrat:wght@400;500;700;800&family=Oswald:wght@600;700&display=swap" rel="stylesheet">
<style>
  :root {
    --backdrop: #1d1f27;
    --paper: #ffffff;
    --navy: #41516f;
    --navy-deep: #344e6e;
    --peach: #dfa688;
    --peach-bright: #eba581;
    --mist: #efeff0;
    --photo-a: #d9d8d6;
    --photo-b: #b8a89a;
  }
  * { margin: 0; padding: 0; box-sizing: border-box; }
  html, body { width: 956px; height: 1200px; overflow: hidden; background: var(--backdrop); }
  body { position: relative; font-family: "Montserrat", sans-serif; }

  .poster {
    position: absolute; left: 148px; top: 91px;
    width: 660px; height: 1018px;
    background: var(--paper); overflow: hidden;
  }
  .poster-shapes { position: absolute; inset: 0; width: 660px; height: 1018px; }

  .brand {
    position: absolute; left: 25px; top: 38px;
    display: flex; align-items: center; gap: 12px;
  }
  .brand-mark { width: 30px; height: 30px; background: var(--navy-deep); }
  .brand-name {
    font-weight: 500; font-size: 50px; line-height: 1;
    color: var(--navy-deep); letter-spacing: -1px;
  }

  .headline {
    position: absolute; left: 24px; top: 148px;
    font-weight: 800; font-size: 42px; line-height: 45px;
    color: var(--navy-deep); letter-spacing: -0.5px;
  }
  .headline .accent { color: var(--peach-bright); display: block; }

  .promise {
    position: absolute; left: 24px; top: 243px; width: 250px; height: 81px;
    padding: 9px 0 0 12px;
    font-weight: 700; font-size: 15.5px; line-height: 21.5px; color: #fff;
  }
  .promise .accent { color: var(--peach-bright); }

  .value { position: absolute; height: 60px; width: 506px; }
  .value-banner {
    position: absolute; left: 0; top: 0; width: 506px; height: 60px;
  }
  .value-text {
    position: absolute; left: 14px; right: 30px; top: 0; height: 60px;
    display: flex; align-items: center;
    font-size: 11.7px; line-height: 16.3px;
  }
  .value.dark .value-text { color: #fff; }
  .value.light .value-text { color: var(--navy); }

  .value-badge {
    position: absolute; width: 64px; height: 71px;
    display: flex; align-items: center; justify-content: center;
    font-family: "Oswald", sans-serif; font-weight: 700;
  }
  .value-badge svg { position: absolute; inset: 0; }
  .value-badge .word { position: relative; display: flex; align-items: baseline; }
  .value-badge .initial { font-size: 24px; line-height: 1; }
  .value-badge .rest { font-size: 7.5px; letter-spacing: 0.2px; }
  .value-badge.peach { color: var(--navy); }
  .value-badge.navy { color: var(--peach); }

  .web {
    position: absolute; left: 0; right: 0; top: 979px;
    text-align: center; color: #fff;
    font-size: 25px; letter-spacing: 2.2px; font-weight: 400;
  }
</style>
</head>
<body>
<main class="poster">
  <svg class="poster-shapes" viewBox="0 0 660 1018" aria-hidden="true">
    <defs>
      <linearGradient id="photoTone" x1="0" y1="0" x2="1" y2="1">
        <stop offset="0" stop-color="#e4e3e1"/>
        <stop offset="0.55" stop-color="#c9c4bf"/>
        <stop offset="1" stop-color="#a88a6c"/>
      </linearGradient>
    </defs>
    <polygon points="372,398 660,398 660,1018 35,1018" fill="var(--mist)"/>
    <path d="M0,1010 L318,929 Q328,926 338,929 L660,1010 L660,1018 L0,1018 Z" fill="var(--navy)"/>
    <path d="M24,250 Q24,243 31,243 L274,243 L226,324 L31,324 Q24,324 24,317 Z" fill="var(--navy)"/>
  </svg>

  <svg class="poster-shapes" viewBox="0 0 660 1018" role="img" aria-label="Photograph of a smiling carer in blue scrubs greeting an elderly resident seated at a table with breakfast">
    <path d="M410,0 L660,0 L660,385 L206,385 Q194,385 200,372 Z" fill="url(#photoTone)"/>
  </svg>

  <div class="brand">
    <span class="brand-mark"></span>
    <span class="brand-name">HALDEN</span>
  </div>

  <h1 class="headline">CARING FOR<span class="accent">YOUR LIFE</span></h1>

  <p class="promise">IN A <span class="accent">SAFE, SECURE AND<br>WELCOMING</span><br>ENVIRONMENT</p>

  <!-- Purpose -->
  <div class="value dark" style="left:84px; top:415px;">
    <svg class="value-banner" viewBox="0 0 506 60" preserveAspectRatio="none" aria-hidden="true"><path d="M6,0 L490,0 Q494,0 495,4 L506,56 Q506,60 502,60 L6,60 Q2,60 3,56 L6,30 L2,4 Q2,0 6,0 Z" fill="var(--navy)"/></svg>
    <p class="value-text">We are driven by a clear understanding of why we do what we do: to enrich lives, honour legacies and make a meaningful difference every day, for our residents, their families, our colleagues and our community.</p>
  </div>
  <div class="value-badge peach" style="left:18px; top:398px;">
    <svg viewBox="0 0 64 71" aria-hidden="true"><polygon points="32,0 64,18 64,53 32,71 0,53 0,18" fill="var(--peach)"/></svg>
    <span class="word"><span class="initial">P</span><span class="rest">URPOSE</span></span>
  </div>

  <!-- Excellence -->
  <div class="value light" style="left:134px; top:499px;">
    <svg class="value-banner" viewBox="0 0 506 60" preserveAspectRatio="none" aria-hidden="true"><path d="M6,0 L490,0 Q494,0 495,4 L506,56 Q506,60 502,60 L6,60 Q2,60 3,56 L6,30 L2,4 Q2,0 6,0 Z" fill="var(--peach)"/></svg>
    <p class="value-text">We hold ourselves to the highest standards, delivering exceptional care and creating an environment where both residents and staff can thrive.</p>
  </div>
  <div class="value-badge navy" style="left:68px; top:482px;">
    <svg viewBox="0 0 64 71" aria-hidden="true"><polygon points="32,0 64,18 64,53 32,71 0,53 0,18" fill="var(--navy)"/></svg>
    <span class="word"><span class="initial">E</span><span class="rest">XCELLENCE</span></span>
  </div>

  <!-- Openness -->
  <div class="value dark" style="left:84px; top:583px;">
    <svg class="value-banner" viewBox="0 0 506 60" preserveAspectRatio="none" aria-hidden="true"><path d="M6,0 L490,0 Q494,0 495,4 L506,56 Q506,60 502,60 L6,60 Q2,60 3,56 L6,30 L2,4 Q2,0 6,0 Z" fill="var(--navy)"/></svg>
    <p class="value-text">We build trust through honest, respectful communication, welcoming feedback, sharing ideas, and embracing change as a path to continuous growth.</p>
  </div>
  <div class="value-badge peach" style="left:18px; top:566px;">
    <svg viewBox="0 0 64 71" aria-hidden="true"><polygon points="32,0 64,18 64,53 32,71 0,53 0,18" fill="var(--peach)"/></svg>
    <span class="word"><span class="initial">O</span><span class="rest">PENNESS</span></span>
  </div>

  <!-- Passion -->
  <div class="value light" style="left:134px; top:667px;">
    <svg class="value-banner" viewBox="0 0 506 60" preserveAspectRatio="none" aria-hidden="true"><path d="M6,0 L490,0 Q494,0 495,4 L506,56 Q506,60 502,60 L6,60 Q2,60 3,56 L6,30 L2,4 Q2,0 6,0 Z" fill="var(--peach)"/></svg>
    <p class="value-text">We are passionate about delivering exceptional care. We take pride in what we do and in making a real difference in people’s lives.</p>
  </div>
  <div class="value-badge navy" style="left:68px; top:650px;">
    <svg viewBox="0 0 64 71" aria-hidden="true"><polygon points="32,0 64,18 64,53 32,71 0,53 0,18" fill="var(--navy)"/></svg>
    <span class="word"><span class="initial">P</span><span class="rest">ASSION</span></span>
  </div>

  <!-- Learning -->
  <div class="value dark" style="left:84px; top:752px;">
    <svg class="value-banner" viewBox="0 0 506 60" preserveAspectRatio="none" aria-hidden="true"><path d="M6,0 L490,0 Q494,0 495,4 L506,56 Q506,60 502,60 L6,60 Q2,60 3,56 L6,30 L2,4 Q2,0 6,0 Z" fill="var(--navy)"/></svg>
    <p class="value-text">We are committed to personal and professional growth; empowering each other through ongoing development, reflection, and shared knowledge.</p>
  </div>
  <div class="value-badge peach" style="left:18px; top:735px;">
    <svg viewBox="0 0 64 71" aria-hidden="true"><polygon points="32,0 64,18 64,53 32,71 0,53 0,18" fill="var(--peach)"/></svg>
    <span class="word"><span class="initial">L</span><span class="rest">EARNING</span></span>
  </div>

  <!-- Empathy -->
  <div class="value light" style="left:134px; top:836px;">
    <svg class="value-banner" viewBox="0 0 506 60" preserveAspectRatio="none" aria-hidden="true"><path d="M6,0 L490,0 Q494,0 495,4 L506,56 Q506,60 502,60 L6,60 Q2,60 3,56 L6,30 L2,4 Q2,0 6,0 Z" fill="var(--peach)"/></svg>
    <p class="value-text">We actively listen and seek to understand before being understood, recognising the unique stories, feelings, and needs of others.</p>
  </div>
  <div class="value-badge navy" style="left:68px; top:819px;">
    <svg viewBox="0 0 64 71" aria-hidden="true"><polygon points="32,0 64,18 64,53 32,71 0,53 0,18" fill="var(--navy)"/></svg>
    <span class="word"><span class="initial">E</span><span class="rest">MPATHY</span></span>
  </div>

  <p class="web">haldenhealthcare.co.uk</p>
</main>
</body>
</html>
```